2 guided dives on the North of Bonaire

2 guided shore dives on the North of Bonaire including authentic local lunch and drinks.
We offer an adventure for experienced divers to discover the dive sites on the north of the island.
Showing you the beauty of the reefs and tasting authentic local cuisine like goat or iguana combined with a stunning view of the surroundings.

Target Market(s)

Divers / tourism

Industry/Entity Type

Tourism / Diving

Font styles to use
Sans Serif

Colors
0054AA
0677BA
7BADD7
CADEEF
E8F1F8
0094D4
00A9DD
6FCCEA
C7EBF8
E9F6FB
F0912C
F2A743
F7CA91
FBE8D2
FDF5EE
EE7325
F08F49
F5BC92
FAE3D3
FDF4ED

Requirements
Must have
• Some of the pictures I uploaded and the food picture / bottom like in the pictures
Nice to have
• inviting to join us on the guided dives
Should not have
• Any picture I didn't provide

```html
<!DOCTYPE html>
<html lang="en">
<head>
<meta charset="utf-8">
<title>Reef Route – Guided Dives North Bonaire</title>
<link rel="stylesheet" href="https://fonts.googleapis.com/css2?family=Archivo:wght@500;700;800&family=Archivo+Black&family=Caveat+Brush&family=Poppins:wght@800&display=swap">
<style>
  :root{
    --navy:#22324f;
    --orange:#e2a64a;
    --gold:#9c6a1c;
    --sky:#a9cdef;
    --white:#ffffff;
    --ink:#111111;
    --web-blue:#3d6fc2;
  }
  *{box-sizing:border-box;margin:0;padding:0}
  html,body{width:881px;height:1200px;overflow:hidden;background:#ffffff}
  .flyer{position:relative;width:881px;height:1200px;overflow:hidden;background:var(--orange);font-family:"Archivo",sans-serif}
  .hero-photo{position:absolute;left:0;top:0;width:881px;height:480px;
    background:linear-gradient(180deg,#4f86d6 0%,#8fb7ea 30%,#2752b0 34%,#3f74c0 48%,#9aa2a4 58%,#8b8a84 100%)}
  .shapes{position:absolute;left:0;top:0}
  .photo-card{position:absolute;border:5px solid var(--white);box-shadow:0 3px 8px rgba(0,0,0,.35)}
  .photo-card--beach{left:-6px;top:448px;width:222px;height:212px;transform:rotate(-6deg);
    background:linear-gradient(180deg,#6fa6e6 0%,#cfe1f5 50%,#3fb0c9 62%,#e9e2d2 78%,#d9cfba 100%)}
  .photo-card--lagoon{left:218px;top:462px;width:222px;height:200px;transform:rotate(3deg);
    background:linear-gradient(180deg,#6f9fe2 0%,#c7dbf2 40%,#5d7a4c 48%,#4a7bd0 62%,#5b8ad8 100%)}
  .photo-card--food{left:432px;top:458px;width:228px;height:196px;transform:rotate(-4deg);
    background:radial-gradient(circle at 40% 60%,#d89a4c 0%,#b5612c 45%,#5a3a26 100%)}
  .photo-card--seahorse{left:660px;top:466px;width:226px;height:190px;transform:rotate(2deg);
    background:linear-gradient(135deg,#2d5f70 0%,#6b2a2f 35%,#3a7b8c 60%,#b08060 80%,#2a5560 100%)}
  .headline{position:absolute;left:42px;font-family:"Caveat Brush",cursive;line-height:1}
  .headline--top{top:686px;font-size:100px;color:var(--sky)}
  .headline--bottom{top:780px;font-size:74px;color:var(--white)}
  .dive-count{position:absolute;left:440px;top:658px;font-family:"Poppins",sans-serif;font-weight:800;font-size:118px;line-height:1;color:var(--white);-webkit-text-stroke:5px var(--navy)}
  .offer-title{position:absolute;left:520px;top:690px;font-weight:800;font-size:19.5px;letter-spacing:1.6px;line-height:1.2}
  .offer-title__line{display:block;color:var(--ink);padding-left:2px}
  .offer-title__line--accent{color:var(--gold);margin-left:-6px}
  .perk{position:absolute;left:440px;display:flex;align-items:flex-start;gap:14px}
  .perk--one{top:812px}
  .perk--two{top:880px}
  .perk__icon{position:relative;flex:none;width:40px;height:40px;border-radius:50%;background:#eef2f7;overflow:hidden}
  .perk__badge{position:absolute;width:16px;height:16px;border-radius:50%;background:var(--navy);color:var(--white);font-size:10px;font-weight:700;display:flex;align-items:center;justify-content:center}
  .perk__text{font-size:19.5px;letter-spacing:1.3px;color:var(--ink);line-height:1.3;width:345px;padding-top:6px}
  .call-to-action{position:absolute;left:0;width:910px;top:1000px;text-align:center;font-family:"Archivo Black",sans-serif;font-size:31px;letter-spacing:2px;color:var(--navy)}
  .brand{position:absolute;left:44px;top:1088px;display:flex;align-items:center;gap:8px;font-weight:800;font-size:22px;color:var(--orange)}
  .brand__dot{width:18px;height:18px;border-radius:50%;background:var(--orange)}
  .included{position:absolute;display:flex;gap:8px;color:var(--white);font-size:13px;letter-spacing:.8px;line-height:1.35}
  .included--dives{left:237px;top:1072px}
  .included--food{left:510px;top:1070px}
  .tick{flex:none;width:15px;height:15px;margin-top:2px}
  .button{position:absolute;top:1117px;height:40px;border-radius:7px;display:flex;align-items:center;font-weight:800;font-size:17.5px}
  .button--call{left:243px;width:279px;background:var(--orange);color:var(--navy);padding-left:8px;gap:4px}
  .button--web{left:531px;width:263px;background:var(--web-blue);color:var(--white);padding-left:22px;gap:10px;font-size:17px}
</style>
</head>
<body>
<main class="flyer">
  <div class="hero-photo" role="img" aria-label="Rocky north coast of Bonaire with limestone cliffs, a stony beach and deep blue sea under a blue sky"></div>

  <svg class="shapes" width="881" height="1200" viewBox="0 0 881 1200" aria-hidden="true">
    <polygon fill="#22324f" points="0,620 470,600 455,660 430,700 440,760 428,830 412,900 230,905 120,918 0,920"/>
    <polygon fill="#ffffff" points="372,672 520,668 881,660 881,772 700,776 560,782 420,776 380,770 392,740 386,700"/>
    <rect fill="#ffffff" x="500" y="786" width="200" height="3" rx="1.5"/>
    <rect fill="#ffffff" x="720" y="782" width="140" height="3" rx="1.5"/>
    <rect fill="#ffffff" x="420" y="662" width="260" height="3" rx="1.5"/>
    <polygon fill="#22324f" points="0,1012 220,1004 300,1016 520,1008 700,1002 881,990 881,1200 0,1200"/>
    <polygon fill="#a9cdef" points="232,1000 300,988 620,986 668,996 650,1018 672,1040 420,1046 250,1040 270,1022"/>
    <rect fill="#a9cdef" x="680" y="1010" width="90" height="3" rx="1.5"/>
    <rect fill="#a9cdef" x="300" y="1050" width="180" height="2.5" rx="1.2"/>
  </svg>

  <div class="photo-card photo-card--beach" role="img" aria-label="White sand beach under a palm-leaf shade with turquoise water"></div>
  <div class="photo-card photo-card--lagoon" role="img" aria-label="Calm blue lagoon with a green hillside and cactus"></div>
  <div class="photo-card photo-card--food" role="img" aria-label="Plates of authentic local food with stews, fried plantain and fries"></div>
  <div class="photo-card photo-card--seahorse" role="img" aria-label="Seahorse clinging to a red pier post underwater"></div>

  <h1 class="headline headline--top">Let Us</h1>
  <p class="headline headline--bottom">Guide you!</p>

  <div class="dive-count">2</div>
  <h2 class="offer-title">
    <span class="offer-title__line">Guided Dives at The</span>
    <span class="offer-title__line offer-title__line--accent">North side of Bonaire</span>
  </h2>

  <div class="perk perk--one">
    <div class="perk__icon">
      <svg width="40" height="40" viewBox="0 0 40 40"><path d="M0 24 Q10 18 20 24 T40 24 V40 H0Z" fill="#22324f"/><path d="M4 30 Q12 26 20 30 T36 30" stroke="#eef2f7" stroke-width="2" fill="none"/></svg>
      <span class="perk__badge" style="right:-1px;top:-1px">1</span>
    </div>
    <p class="perk__text">We show you the cool stuff</p>
  </div>
  <div class="perk perk--two">
    <div class="perk__icon">
      <svg width="40" height="40" viewBox="0 0 40 40"><path d="M2 22 Q12 16 22 22 T42 22" stroke="#22324f" stroke-width="3" fill="none"/><path d="M2 30 Q12 24 22 30 T42 30" stroke="#22324f" stroke-width="3" fill="none"/></svg>
      <span class="perk__badge" style="right:-1px;top:-1px">2</span>
    </div>
    <p class="perk__text">You just enjoy the dives, we take care of the rest</p>
  </div>

  <p class="call-to-action">JOIN US NOW!</p>

  <div class="brand"><span class="brand__dot"></span>Reef Route</div>

  <div class="included included--dives">
    <svg class="tick" viewBox="0 0 16 16"><circle cx="8" cy="8" r="8" fill="#e2a64a"/><path d="M4.5 8.2l2.3 2.3 4.7-4.7" stroke="#fff" stroke-width="1.8" fill="none"/></svg>
    <span>Two guided dives at Klein<br>Bonaire / North Coast</span>
  </div>
  <div class="included included--food">
    <svg class="tick" viewBox="0 0 16 16"><circle cx="8" cy="8" r="8" fill="#e2a64a"/><path d="M4.5 8.2l2.3 2.3 4.7-4.7" stroke="#fff" stroke-width="1.8" fill="none"/></svg>
    <span>Lunch, fruit, premium open bar and<br>deluxe BBQ-diner is included</span>
  </div>

  <div class="button button--call">
    Call us
    <svg width="20" height="20" viewBox="0 0 20 20"><circle cx="10" cy="10" r="10" fill="#ffffff"/><path d="M6.5 5.5l2 .2.8 2.2-1.2 1a6 6 0 0 0 3 3l1-1.2 2.2.8.2 2c-4.5.5-8.5-3.5-8-8z" fill="#e2a64a"/></svg>
    +(599) 700 12 34
  </div>
  <div class="button button--web">
    <svg width="26" height="26" viewBox="0 0 26 26" fill="none" stroke="#ffffff" stroke-width="1.6"><circle cx="13" cy="13" r="11"/><ellipse cx="13" cy="13" rx="5" ry="11"/><path d="M2 13h22M4 7h18M4 19h18"/></svg>
    www.reefroute-dive.com
  </div>
</main>
</body>
</html>
```